Zielgruppe
wir suchen ein hochwertiges Design für ein Buchcover (Deutsch und English). Zielgruppe sind Teenager ab 13 Jahre.
Aufgabenstellung
es geht um ein Buch für Codes welche geknackt werden sollen. die Codes sind von verschiedenen Typen und Arten mit dem Ziel mathematische Fähigkeiten und logisches Denken sowie Mustererkennung zu fördern. thinking out of the box ist ein sehr wichtiges Aspekt des Buches, wo der Leser gefordert wird, unkonventionell zu denken.
Beispiele über codes sowie erste Coverentwürfe finden Sie im Anhang
Buchtitel (DE/EN) : Kopfnuss Pfad / puzzle trail
Abmessungen : 13.97 x 0.43 x 21.59 cm [(5,5x8,5) inches]
Seiten: 72
Cover soll mit Vornex PBL Anforderungen kompatibel sein

```html
<!DOCTYPE html>
<html lang="de">
<head>
<meta charset="utf-8">
<title>Kopfnuss Pfad – Buchcover</title>
<link rel="stylesheet" href="https://fonts.googleapis.com/css2?family=Bebas+Neue&family=Montserrat:wght@400;500&family=Open+Sans:wght@400&display=swap">
<style>
  :root {
    --cover-orange: #ec7535;
    --cover-shadow: #d4652c;
    --title-white: #ffffff;
    --subtitle-navy: #213656;
    --figure-light: #e6e3ea;
    --figure-mid: #b9b5c0;
  }
  html, body {
    margin: 0;
    padding: 0;
    width: 837px;
    height: 1200px;
    overflow: hidden;
    background: var(--cover-orange);
  }
  .cover {
    position: relative;
    width: 837px;
    height: 1200px;
    background: var(--cover-orange);
    overflow: hidden;
  }
  .title-word {
    position: absolute;
    right: 126px;
    margin: 0;
    font-family: "Bebas Neue", sans-serif;
    font-weight: 400;
    font-size: 186px;
    line-height: 1;
    color: var(--title-white);
    letter-spacing: 2px;
    white-space: nowrap;
  }
  .title-word--top { top: 28px; }
  .title-word--bottom { top: 231px; }
  .subtitle {
    position: absolute;
    right: 116px;
    margin: 0;
    font-family: "Montserrat", sans-serif;
    font-weight: 500;
    color: var(--subtitle-navy);
    line-height: 1;
    white-space: nowrap;
  }
  .subtitle--training { top: 178px; font-size: 47px; }
  .subtitle--audience { top: 383px; right: 124px; font-size: 47px; }
  .illustration {
    position: absolute;
    left: 107px;
    top: 478px;
    width: 630px;
    height: 478px;
    border-radius: 48% 52% 45% 55% / 55% 50% 50% 45%;
    background: radial-gradient(ellipse at 55% 40%, var(--figure-light) 0%, var(--figure-mid) 70%, rgba(185,181,192,0) 100%);
  }
  .floor-shadow {
    position: absolute;
    left: 300px;
    top: 950px;
    width: 260px;
    height: 70px;
    border-radius: 50%;
    background: radial-gradient(ellipse, var(--cover-shadow) 0%, rgba(212,101,44,0) 70%);
  }
  .tagline {
    position: absolute;
    left: 0;
    width: 806px;
    margin: 0;
    text-align: center;
    font-family: "Open Sans", sans-serif;
    color: var(--title-white);
    line-height: 1;
  }
  .tagline--headline { top: 1014px; font-size: 31px; letter-spacing: 0.5px; }
  .tagline--body { top: 1060px; font-size: 22px; line-height: 32px; }
  .author {
    position: absolute;
    left: 0;
    width: 806px;
    top: 1140px;
    margin: 0;
    text-align: center;
    font-family: "Open Sans", sans-serif;
    font-size: 30px;
    color: var(--title-white);
    line-height: 1;
  }
</style>
</head>
<body>
  <main class="cover">
    <h1 class="title-word title-word--top">KOPFNUSS</h1>
    <p class="subtitle subtitle--training">Gedächtnistraining</p>
    <h1 class="title-word title-word--bottom">PFAD</h1>
    <p class="subtitle subtitle--audience">für Jugendliche</p>

    <div class="floor-shadow"></div>
    <div class="illustration" role="img" aria-label="Illustration: ein laufendes Gehirn mit Armen, Beinen und hellblauen Turnschuhen"></div>

    <p class="tagline tagline--headline">UNKONVENTIONELL DENKEN</p>
    <p class="tagline tagline--body">Die Aufgaben fördern mathematische Fähigkeiten,<br>logisches Denken und Mustererkennung</p>
    <p class="author">Quimsel</p>
  </main>
</body>
</html>
```